Stationery Design Project

Belo:

Thank you! LOVE your work here. Now, we'd like 1. letterhead and 2. business card designs. Additionally, how do I get the name of the fonts you used in our selected "logo" 1130948?

1. Pls. include our address:

48 Carrow Lane
New York, NY 10418

2. our contact numbers:

212-555-4130
800-555-6172
fax 212-555-4187

3. maybe include:

www.pembrick.net

4. maybe inlcude (maybe not on business cards if too much):

Member: QMEX, OLDUC, RVB, QMEX VORTA, TMGU

5. business cards must obviously have name, title and email

Again, thank you very much for your fantastic work. You've been so responsive to us.

Please contact me directly with any questions you have at:
tdowney@pembrick.net

Belo:

For the business card, please use myinformation as a relevant example:

Tessa Downey
HR Administrator

48 Carrow Lane
New York, NY  10006
212-555-3021
800-555-6172
f 212-555-4184
tdowney@pembrick.net

If room, on the card:
www.pembrick.net

and also if room on the card relating to the firm NOT me:

Member of:  QMEX, OLDUC, RVB, QMEX VORTA, TMGU

Belo:

Tessa Downey
HR Administrator

48 Carrow Lane
New York, NY  10006
212-555-3021
800-555-6172
f 212-555-4184
tdowney@pembrick.net

If room, on the card:
www.pembrick.net

Belo:

What are the fonts you used for our Pembrick & Loman?

And the font you used for our Investment Management Since 1924?

Again, thank you for your help and please contact me directly at tdowney@pembrick.net

:-)

Target Market(s)

High-net worth individuals and clients

Industry/Entity Type

Business

Requirements
Must have
• Letterhead:
address
contact numbers
web site

Business cards:
name and title
address
contct numbers
email
Nice to have
• Letter head:

Business card:
website

```html
<!DOCTYPE html>
<html lang="en">
<head>
<meta charset="utf-8">
<title>Pembrick &amp; Loman Stationery</title>
<link href="https://fonts.googleapis.com/css2?family=Libre+Baskerville&family=Open+Sans:wght@400;600&display=swap" rel="stylesheet">
<style>
  :root {
    --bg: #f4f4f4;
    --paper: #ffffff;
    --navy: #1f3a78;
    --name-blue: #1a4fb0;
    --ink: #555555;
    --fine: #777777;
    --flap: #a9a9a9;
    --window: #e1e1e1;
    --dark-a: #8b8a86;
    --dark-b: #4e4e4e;
  }
  * { margin: 0; padding: 0; box-sizing: border-box; }
  html, body { width: 1200px; height: 1039px; overflow: hidden; }
  body {
    background: radial-gradient(ellipse at 50% 40%, #ffffff 0%, var(--bg) 70%);
    font-family: "Open Sans", sans-serif;
    position: relative;
  }
  .sheet { position: absolute; background: var(--paper); box-shadow: 0 1px 5px rgba(0,0,0,.28); }
  .wordmark {
    position: absolute;
    font-family: "Libre Baskerville", serif;
    color: var(--navy);
    white-space: nowrap;
    letter-spacing: .2px;
  }
  .fine { position: absolute; font-size: 6.3px; color: var(--fine); text-align: right; line-height: 9.5px; white-space: nowrap; }

  /* letterhead */
  .letterhead { left: 47px; top: 111px; width: 511px; height: 626px; }
  .letterhead .wordmark { right: 28px; top: 31px; font-size: 19px; }
  .letterhead .address { right: 28px; top: 72px; }
  .letter-body {
    position: absolute; left: 73px; top: 163px; width: 400px;
    font-size: 9.3px; line-height: 12.55px; color: var(--ink);
  }
  .signature { position: absolute; right: 47px; top: 438px; font-size: 16px; color: var(--ink); }
  .letterhead .footer { right: 28px; bottom: 34px; }

  /* business card front */
  .card-front { left: 586px; top: 95px; width: 359px; height: 223px; }
  .card-front .wordmark { right: 26px; top: 25px; font-size: 22px; }
  .card-front .address { right: 25px; top: 81px; }
  .holder { position: absolute; right: 25px; top: 124px; text-align: right; color: var(--name-blue); }
  .holder-name { font-size: 18.5px; font-weight: 600; line-height: 22px; }
  .holder-title { font-size: 9.3px; line-height: 11px; }
  .card-front .contact { right: 25px; bottom: 15px; font-size: 7.2px; }

  /* business card back */
  .card-back { left: 785px; top: 324px; width: 358px; height: 223px; background: linear-gradient(90deg, var(--dark-a), var(--dark-b)); }
  .card-back .wordmark { left: 0; right: 0; top: 94px; text-align: center; font-size: 20px; color: #ffffff; }

  /* note card */
  .note-card { left: 745px; top: 557px; width: 358px; height: 223px; background: linear-gradient(180deg, #ffffff 0%, #e8e8e8 100%); }
  .note-card .wordmark { left: 0; right: 0; top: 92px; text-align: center; font-size: 21px; }

  /* envelope */
  .envelope { left: 254px; top: 760px; width: 564px; height: 257px; }
  .envelope-flap { position: absolute; left: 254px; top: 723px; width: 564px; height: 37px; }
  .envelope .wordmark { left: 42px; top: 44px; font-size: 17.5px; }
  .envelope .address { right: 19px; top: 24px; }
  .address-window { position: absolute; left: 36px; top: 77px; width: 199px; height: 67px; background: var(--window); }
</style>
</head>
<body>

  <section class="sheet letterhead">
    <div class="wordmark">PEMBRICK &amp; LOMAN</div>
    <p class="fine address">48 Carrow Lane, New York, NY 10418<br>212-555-4130 | 800-555-2094 | Fax: 212-555-4187</p>
    <p class="letter-body">
      Lorem ipsum dolor sit amet, consectetuer adipiscing elit. Cum sociis natoque<br>
      penatibus et magnis dis urient montes, nascetur ridiculus mus. Sed nonummy,<br>
      sem rhoncus tempor accumsan, justo enim bibendum ipsum, eget sagittis nc felis<br>
      sed orci. Morbi mi eros, ultrices vitae, consequat nec, consequat at, augue. Class<br>
      aptent taciti sociosqu ad litora torquent per conubia nostra, per inceptos hyme-<br>
      naeos. Fusce dapibus sapien eu nunc.Lorem ipsum dolor sit amet, consectetuer<br>
      iscing elit. Cum sociis natoque penatibus et magnis dis parturient montes, nasce-<br>
      tur ridiculus mus. Sed nonummy, sem rhoncus empor accumsan, justo enim<br>
      bibendum ipsum, eget sagittis nunc felis sed orci. Morbi mi eros, ultrices vitae,<br>
      consequat nec, consequat at, augue. Class aptent taciti sociosqu ad litora<br>
      torquent per conubia nostra, per inceptos hymenaeos. Fusce pibus sapien eu<br>
      nunc.Lorem ipsum dolor sit amet, consectetuer adipiscing elit. Cum sociis<br>
      natoque penatibus et magnis dis arturient montes, nascetur ridiculus mus. Sed<br>
      nmy, sem rhoncus tempor accumsan,. magnis dis urient montes, nascetur ridicu-<br>
      lus mus. Sed nonummy, sem rhoncus tempor accumsan, justo enim bibendum<br>
      ipsum, eget sagittis nc felis sed orci. Morbi mi eros, ultrices vitae, consequat nec,<br>
      consequat at, augue. Class aptent taciti sociosqu ad litora torquent per conubia<br>
      nostra, per inceptos hymenaeos. Fusce dapibus sapien eu nunc.Lorem ipsum<br>
      dolor sit amet, consectetuer iscing elit. Cum sociis natoque penatibus et magnis<br>
      dis partuv
    </p>
    <p class="signature">Your Signature</p>
    <p class="fine footer">E: tdowney@pembrick.net | Member : QMEX, OLDUC, RVB, QMEX VORTA, TMGU</p>
  </section>

  <section class="sheet card-front">
    <div class="wordmark">PEMBRICK &amp; LOMAN</div>
    <p class="fine address">48 Carrow Lane, New York, NY 10418<br>212-555-4130 | 800-555-2094 | F: 212-555-4187</p>
    <div class="holder">
      <p class="holder-name">Tessa Downey</p>
      <p class="holder-title">HR Administrator</p>
    </div>
    <p class="fine contact">E: tdowney@pembrick.net | W: www.pembrick.net</p>
  </section>

  <section class="sheet card-back">
    <div class="wordmark">PEMBRICK &amp; LOMAN</div>
  </section>

  <section class="sheet note-card">
    <div class="wordmark">PEMBRICK &amp; LOMAN</div>
  </section>

  <svg class="envelope-flap" width="564" height="37" viewBox="0 0 564 37" aria-hidden="true">
    <polygon points="37,0 527,0 564,37 0,37" fill="var(--flap)"/>
  </svg>
  <section class="sheet envelope">
    <p class="fine address">48 Carrow Lane, New York, NY 10418</p>
    <div class="wordmark">PEMBRICK &amp; LOMAN</div>
    <div class="address-window"></div>
  </section>

</body>
</html>
```